Brindale transport business cards

Front of card, Looking for my logo on one side of the card

Back of card,
Brindale Transport Maintenance
Onsite Cars, Trucks & trailer maintenance and repairs
Ronan Brindale
0452819036
Brindaletm@fernmail.com

```html
<!DOCTYPE html>
<html lang="en">
<head>
<meta charset="utf-8">
<title>Brindale transport business cards</title>
<link href="https://fonts.googleapis.com/css2?family=Montserrat:wght@400;500;700;800&display=swap" rel="stylesheet">
<style>
  :root {
    --page-bg: #1c1c1d;
    --card-bg: #2a2a2c;
    --card-shadow: rgba(0, 0, 0, 0.55);
    --brand-blue: #1a6fd6;
    --brand-blue-deep: #0d3f8c;
    --silver: #c9c9cc;
    --text-light: #ffffff;
    --text-soft: #e6e6e8;
  }
  * { margin: 0; padding: 0; box-sizing: border-box; }
  html, body {
    width: 1200px;
    height: 900px;
    overflow: hidden;
    background: var(--page-bg);
    font-family: "Montserrat", sans-serif;
  }
  .card {
    position: absolute;
    left: 250px;
    width: 700px;
    height: 400px;
    border-radius: 22px;
    background: var(--card-bg);
    overflow: hidden;
    box-shadow: 0 18px 40px var(--card-shadow);
  }
  .card--front { top: 30px; }
  .card--back { top: 470px; }

  /* Front */
  .front-artwork {
    position: absolute;
    left: 120px;
    top: 30px;
    width: 460px;
    height: 300px;
    border-radius: 12px;
    background: radial-gradient(ellipse at 45% 45%, rgba(26, 111, 214, 0.28), rgba(42, 42, 44, 0) 70%);
  }
  .brand-lockup {
    position: absolute;
    left: 0;
    right: 0;
    top: 150px;
    display: flex;
    align-items: center;
    justify-content: center;
    gap: 16px;
  }
  .brand-mark {
    width: 34px;
    height: 34px;
    background: var(--brand-blue);
  }
  .brand-name {
    font-weight: 800;
    font-size: 40px;
    letter-spacing: 1px;
    text-transform: uppercase;
    color: var(--text-light);
    white-space: nowrap;
  }
  .front-band {
    position: absolute;
    left: 0;
    right: 0;
    bottom: 0;
    height: 44px;
    background: linear-gradient(180deg, var(--brand-blue) 0%, var(--brand-blue-deep) 100%);
    border-top: 4px solid var(--silver);
  }

  /* Back */
  .holder {
    position: absolute;
    left: 20px;
    top: 120px;
    width: 330px;
    height: 90px;
    display: flex;
    align-items: center;
    justify-content: flex-end;
    padding-right: 20px;
    font-weight: 800;
    font-size: 28px;
    letter-spacing: 1px;
    color: var(--text-light);
    text-transform: uppercase;
    white-space: nowrap;
  }
  .divider {
    position: absolute;
    left: 350px;
    top: 115px;
    width: 2px;
    height: 100px;
    background: linear-gradient(180deg, rgba(26,111,214,0), var(--brand-blue), rgba(26,111,214,0));
  }
  .contact-list {
    position: absolute;
    left: 372px;
    top: 128px;
    list-style: none;
    color: var(--text-soft);
    font-size: 19px;
    font-weight: 500;
    white-space: nowrap;
  }
  .contact-item {
    display: flex;
    align-items: center;
    gap: 10px;
    height: 36px;
  }
  .contact-icon { width: 18px; height: 18px; flex: none; }
  .company-info {
    position: absolute;
    left: 0;
    right: 0;
    top: 270px;
    text-align: center;
    color: var(--text-soft);
    font-size: 17px;
    line-height: 1.6;
  }
</style>
</head>
<body>

<section class="card card--front">
  <div class="front-artwork" role="img" aria-label="Faint blue truck illustration behind the brand name"></div>
  <div class="brand-lockup">
    <span class="brand-mark"></span>
    <span class="brand-name">Brindale Transport</span>
  </div>
  <div class="front-band"></div>
</section>

<section class="card card--back">
  <div class="holder">Ronan Brindale</div>
  <div class="divider"></div>
  <ul class="contact-list">
    <li class="contact-item">
      <svg class="contact-icon" viewBox="0 0 24 24" aria-hidden="true">
        <path fill="#1a6fd6" d="M6.6 10.8a15.1 15.1 0 0 0 6.6 6.6l2.2-2.2a1 1 0 0 1 1-.25 11.4 11.4 0 0 0 3.6.57 1 1 0 0 1 1 1V20a1 1 0 0 1-1 1A17 17 0 0 1 3 4a1 1 0 0 1 1-1h3.5a1 1 0 0 1 1 1c0 1.25.2 2.45.57 3.57a1 1 0 0 1-.25 1z"/>
      </svg>
      <span>0452819036</span>
    </li>
    <li class="contact-item">
      <svg class="contact-icon" viewBox="0 0 24 24" aria-hidden="true">
        <rect x="2" y="5" width="20" height="14" rx="2" fill="#1a6fd6"/>
        <path d="M3 6l9 7 9-7" fill="none" stroke="#ffffff" stroke-width="1.6"/>
      </svg>
      <span>Brindaletm@fernmail.com</span>
    </li>
  </ul>
  <div class="company-info">
    <p>Brindale Transport Maintenance</p>
    <p>Onsite Cars, Trucks &amp; trailer maintenance and repairs</p>
  </div>
</section>

</body>
</html>
```